Re-branding stationary for Company

Corvane Diamonds is a diamond trading company that has been established since more then 30years.

We are currently looking to re-design our current logo design into something more modern and more appealing the the new generation. Small changes are what we are looking for that will give our company a little more modern look and a new appeal.
The design should be on similar lines to what our current logo is, but we are definitely wanting to have some modern changes to this.
Along with this, we are looking to have design for complete stationary including, business cards, envelopes, letterheads, etc..

Attached is our current logo, can use this as a base point towards creating a new design.
Updates

Project Deadline Extended Reason: Am still looking for wonderful and amazingly creative design for my company, a facelift with a little modern touchHave provided you with a current logo of the company as inspiration to make something new and unique. PLEASE DO NOT USE COPY THE LOGO FILE AS IT IS! Added Wednesday, May 6, 2015

Target Market(s)

We are a company established since over 30 years, and want to maintain our core fundamental values which is portrayed through our logo. Use this as a base into creating new modern design.

Industry/Entity Type

It Company

Font styles to use
Serif
Sans Serif
Decorative
Script

Requirements
Must have
• A modern touch
• Color combination should be similar in terms with what we currently use in attached design.
Nice to have
• Want that the design is appealing using simple but yet modern features to change and restructure the current company logo.
Should not have
• Not looking more multi colored design
• Not gotta be too overly extravagant

```html
<!DOCTYPE html>
<html lang="en">
<head>
<meta charset="utf-8">
<title>Corvane Diamonds – Brand Identity &amp; Stationery</title>
<link rel="stylesheet" href="https://fonts.googleapis.com/css2?family=Montserrat:wght@300;400;500;700&family=Tinos&display=swap">
<style>
  :root {
    --magenta: #e5168f;
    --orchid: #94308f;
    --rose: #e76ba8;
    --midnight: #2a1656;
    --ink: #3b2470;
    --stage: #e9e9eb;
    --paper: #ffffff;
    --night: #060606;
    --slate: #3d3a3b;
    --text: #222222;
    --muted: #8a8a8a;
  }
  * { box-sizing: border-box; margin: 0; padding: 0; }
  html, body { width: 1200px; height: 900px; overflow: hidden; background: var(--stage); }
  body { font-family: "Montserrat", sans-serif; color: var(--text); }
  address { font-style: normal; }
  .canvas { position: relative; width: 1200px; height: 900px; overflow: hidden; background: var(--stage); }

  /* ---------- brand sheet ---------- */
  .brand-sheet { position: absolute; left: 0; top: 0; width: 300px; height: 900px; background: var(--paper); }
  .brand-version { position: absolute; left: 0; width: 300px; display: flex; flex-direction: column; align-items: center; justify-content: center; gap: 8px; }
  .brand-version--light { top: 0; height: 190px; background: var(--paper); }
  .brand-version--black { top: 190px; height: 195px; background: var(--night); }
  .brand-version--slate { top: 385px; height: 193px; background: var(--slate); }
  .wordmark { display: flex; align-items: center; gap: 8px; }
  .wordmark__mark { width: 20px; height: 20px; background: var(--magenta); flex: none; }
  .wordmark__name { font-weight: 500; font-size: 22px; letter-spacing: 0; color: var(--ink); white-space: nowrap; }
  .tagline { font-weight: 400; font-size: 9px; letter-spacing: 1.2px; color: var(--magenta); white-space: nowrap; }
  .brand-version--black .wordmark__name { color: #f2f2f2; }
  .brand-version--black .tagline { color: var(--rose); }
  .brand-version--slate .wordmark__mark { background: transparent; border: 2px solid #f2f2f2; }
  .brand-version--slate .wordmark__name { color: #f2f2f2; }
  .brand-version--slate .tagline { color: #d0d0d0; }

  .palette { position: absolute; top: 586px; left: 0; width: 300px; text-align: center; }
  .section-title { font-weight: 700; font-size: 19px; color: var(--ink); }
  .swatches { display: flex; justify-content: center; gap: 9px; margin-top: 6px; }
  .swatch { width: 36px; }
  .swatch__chip { width: 36px; height: 36px; }
  .swatch__code { font-size: 4px; line-height: 5px; color: var(--muted); margin-top: 3px; text-align: left; }
  .swatch--magenta .swatch__chip { background: var(--magenta); }
  .swatch--orchid .swatch__chip { background: var(--orchid); }
  .swatch--rose .swatch__chip { background: var(--rose); }
  .swatch--midnight .swatch__chip { background: var(--midnight); }

  .type-specimen { position: absolute; top: 682px; left: 0; width: 300px; text-align: center; }
  .type-specimen .wordmark__name { font-size: 14px; display: block; margin-top: 2px; }
  .type-specimen .tagline { font-size: 5.5px; display: block; margin-top: 1px; }
  .specimen-family { font-weight: 700; font-size: 21px; color: var(--ink); margin-top: 4px; }
  .specimen-glyphs { font-weight: 300; font-size: 19px; line-height: 20px; color: var(--rose); }
  .specimen-pangram { font-weight: 300; font-size: 7.5px; line-height: 10px; color: var(--muted); }

  /* ---------- letterhead ---------- */
  .letterhead { position: absolute; left: 330px; top: 190px; width: 400px; height: 566px; background: var(--paper); box-shadow: 0 1px 3px rgba(0,0,0,.12); overflow: hidden; }
  .letterhead__pattern { position: absolute; left: 0; top: 0; width: 400px; height: 536px; }
  .letterhead__logo { position: absolute; top: 40px; right: 32px; display: flex; flex-direction: column; align-items: center; gap: 3px; }
  .letterhead__logo .wordmark { gap: 6px; }
  .letterhead__logo .wordmark__mark { width: 12px; height: 12px; }
  .letterhead__logo .wordmark__name { font-size: 11px; }
  .letterhead__logo .tagline { font-size: 4.6px; }
  .letter { position: absolute; left: 62px; top: 120px; width: 300px; font-family: "Tinos", serif; font-size: 7.4px; line-height: 9.2px; color: var(--text); }
  .letter p { margin-bottom: 9px; text-align: justify; }
  .letter__salutation { margin-bottom: 12px !important; }
  .letter__sign { margin-top: 20px; }
  .letter__footer { position: absolute; left: 62px; top: 470px; font-family: "Tinos", serif; font-size: 6px; line-height: 9px; color: var(--text); }
  .letterhead__band { position: absolute; left: 0; bottom: 0; width: 400px; height: 30px; background: var(--midnight); display: flex; flex-direction: column; align-items: center; justify-content: center; gap: 2px; }
  .letterhead__band .wordmark__name { font-size: 10px; color: #e6e0f0; }
  .letterhead__band .tagline { font-size: 4.4px; color: #b9aed3; }

  /* ---------- envelopes ---------- */
  .envelope { position: absolute; width: 420px; height: 210px; background: var(--paper); box-shadow: 0 1px 3px rgba(0,0,0,.12); overflow: hidden; }
  .envelope--front { left: 750px; top: 120px; }
  .envelope--back { left: 750px; top: 350px; }
  .envelope__pattern { position: absolute; left: 0; top: 0; width: 420px; height: 210px; }
  .envelope__logo { position: absolute; top: 16px; right: 18px; display: flex; flex-direction: column; align-items: center; gap: 3px; }
  .envelope__logo .wordmark { gap: 5px; }
  .envelope__logo .wordmark__mark { width: 10px; height: 10px; }
  .envelope__logo .wordmark__name { font-size: 9.5px; }
  .envelope__logo .tagline { font-size: 4px; }
  .envelope__address { position: absolute; top: 78px; right: 30px; font-size: 6px; line-height: 8px; color: var(--text); text-transform: uppercase; }
  .envelope__address span { display: block; }
  .envelope__address .gap { margin-top: 7px; }
  .envelope__flap { position: absolute; left: 0; top: 0; width: 420px; height: 90px; }
  .envelope__back-logo { position: absolute; left: 200px; top: 168px; display: flex; flex-direction: column; align-items: center; gap: 2px; }
  .envelope__back-logo .wordmark__name { font-size: 8.5px; }
  .envelope__back-logo .tagline { font-size: 3.6px; }

  /* ---------- business cards ---------- */
  .card { position: absolute; top: 610px; width: 200px; height: 116px; background: var(--paper); box-shadow: 0 1px 3px rgba(0,0,0,.14); overflow: hidden; }
  .card--front { left: 750px; display: flex; flex-direction: column; align-items: center; justify-content: center; gap: 4px; }
  .card--front .wordmark { gap: 6px; }
  .card--front .wordmark__mark { width: 12px; height: 12px; }
  .card--front .wordmark__name { font-size: 11px; }
  .card--front .tagline { font-size: 4.6px; }
  .card--back { left: 970px; }
  .card__pattern { position: absolute; left: 0; top: 0; width: 200px; height: 116px; }
  .card__person { position: absolute; right: 12px; top: 16px; text-align: left; width: 82px; }
  .card__name { font-weight: 400; font-size: 9px; color: var(--text); letter-spacing: .4px; }
  .card__role { font-size: 4.5px; color: var(--muted); margin-top: 1px; }
  .card__contacts { position: absolute; left: 118px; top: 52px; list-style: none; font-size: 4.6px; line-height: 9px; color: var(--text); }
  .card__contacts li { display: flex; align-items: center; gap: 4px; }
  .card__contacts svg { width: 5px; height: 5px; fill: var(--text); }
</style>
</head>
<body>
<main class="canvas">

  <!-- Brand sheet -->
  <section class="brand-sheet" aria-label="Brand guidelines">
    <div class="brand-version brand-version--light">
      <div class="wordmark"><span class="wordmark__mark"></span><span class="wordmark__name">Corvane Diamonds</span></div>
      <div class="tagline">FINE STONES TRADING HOUSE</div>
    </div>
    <div class="brand-version brand-version--black">
      <div class="wordmark"><span class="wordmark__mark"></span><span class="wordmark__name">Corvane Diamonds</span></div>
      <div class="tagline">FINE STONES TRADING HOUSE</div>
    </div>
    <div class="brand-version brand-version--slate">
      <div class="wordmark"><span class="wordmark__mark"></span><span class="wordmark__name">Corvane Diamonds</span></div>
      <div class="tagline">FINE STONES TRADING HOUSE</div>
    </div>

    <div class="palette">
      <h2 class="section-title">color</h2>
      <div class="swatches">
        <div class="swatch swatch--magenta"><div class="swatch__chip"></div><p class="swatch__code">C 0 M 95 Y 0 K 0<br>#E5168F</p></div>
        <div class="swatch swatch--orchid"><div class="swatch__chip"></div><p class="swatch__code">C 45 M 90 Y 0 K 0<br>#94308F</p></div>
        <div class="swatch swatch--rose"><div class="swatch__chip"></div><p class="swatch__code">C 5 M 70 Y 0 K 0<br>#E76BA8</p></div>
        <div class="swatch swatch--midnight"><div class="swatch__chip"></div><p class="swatch__code">C 90 M 100 Y 20 K 40<br>#2A1656</p></div>
      </div>
    </div>

    <div class="type-specimen">
      <h2 class="section-title">font</h2>
      <span class="wordmark__name">Corvane Diamonds</span>
      <span class="tagline">FINE STONES TRADING HOUSE</span>
      <p class="specimen-family">Montserrat</p>
      <p class="specimen-glyphs">abcdefghijk<br>lmnopqrstu<br>vwxyz<br>1234567890</p>
      <p class="specimen-pangram">The quick brown fox jumps over the lazy dog<br>The quick brown fox jumps over the lazy dog<br>The quick brown fox jumps over the lazy dog<br>The quick brown fox jumps over the lazy dog</p>
    </div>
  </section>

  <!-- Letterhead -->
  <article class="letterhead" aria-label="Letterhead">
    <svg class="letterhead__pattern" viewBox="0 0 400 536" role="img" aria-label="Faceted geometric pattern in pink, lilac and grey tones">
      <defs>
        <linearGradient id="lh-facets" x1="0" y1="0" x2="0.4" y2="1">
          <stop offset="0" stop-color="#a9a3be"/>
          <stop offset="0.3" stop-color="#d7d2e2"/>
          <stop offset="0.55" stop-color="#e98cbd"/>
          <stop offset="0.75" stop-color="#c9a4c8"/>
          <stop offset="1" stop-color="#a39cb8"/>
        </linearGradient>
      </defs>
      <polygon points="0,0 120,0 50,150 50,330 150,536 0,536" fill="url(#lh-facets)"/>
    </svg>
    <div class="letterhead__logo">
      <div class="wordmark"><span class="wordmark__mark"></span><span class="wordmark__name">Corvane Diamonds</span></div>
      <div class="tagline">FINE STONES TRADING HOUSE</div>
    </div>
    <div class="letter">
      <p class="letter__salutation">DEAR CLIENT</p>
      <p>Lorem ipsum dolor sit amet, consectetuer adipiscing elit, sed diam nonummy nibh euismod tincidunt ut laoreet dolore magna aliquam erat volutpat. Ut wisi enim ad minim veniam, quis nostrud exerci tation ullamcorper suscipit lobortis nisl ut aliquip ex ea commodo consequat.</p>
      <p>Duis autem vel eum iriure dolor in hendrerit in vulputate velit esse molestie consequat, vel illum dolore eu feugiat nulla facilisis at vero eros et accumsan et iusto odio dignissim qui blandit praesent luptatum zzril delenit augue duis dolore te feugait nulla facilisi. Ut wisi enim ad minim veniam, quis nostrud exerci tation ullamcorper suscipit lobortis nisl ut aliquip ex ea commodo consequat. Duis autem vel eum iriure dolor in hendrerit in vulputate velit esse molestie consequat.</p>
      <p>Vel illum dolore eu feugiat nulla facilisis at vero eros et accumsan et iusto odio dignissim qui blandit praesent luptatum zzril delenit augue duis dolore te feugait nulla facilisi. Lorem ipsum dolor sit amet, consectetuer adipiscing elit, sed diam nonummy nibh euismod tincidunt ut laoreet dolore magna aliquam erat volutpat.</p>
      <p>Yours sincerely,</p>
      <p class="letter__sign">OWNER</p>
    </div>
    <address class="letter__footer">Vel illum dolore eu feugiat<br>01 98765430<br>Street Vel illum dolore No. 13</address>
    <div class="letterhead__band">
      <span class="wordmark__name">Corvane Diamonds</span>
      <span class="tagline">FINE STONES TRADING HOUSE</span>
    </div>
  </article>

  <!-- Envelope, front -->
  <article class="envelope envelope--front" aria-label="Envelope front">
    <svg class="envelope__pattern" viewBox="0 0 420 210" role="img" aria-label="Faceted geometric pattern in magenta, purple and pink tones">
      <defs>
        <linearGradient id="env-facets" x1="0" y1="0" x2="1" y2="0.6">
          <stop offset="0" stop-color="#3a1f63"/>
          <stop offset="0.35" stop-color="#c21b86"/>
          <stop offset="0.6" stop-color="#e35fa6"/>
          <stop offset="1" stop-color="#a89bc0"/>
        </linearGradient>
      </defs>
      <polygon points="0,0 130,0 110,60 215,210 0,210" fill="url(#env-facets)"/>
    </svg>
    <div class="envelope__logo">
      <div class="wordmark"><span class="wordmark__mark"></span><span class="wordmark__name">Corvane Diamonds</span></div>
      <div class="tagline">FINE STONES TRADING HOUSE</div>
    </div>
    <address class="envelope__address">
      <span>To: Mr. Alden Voss</span>
      <span>Lorem ipsum street</span>
      <span>Lorem ipsum city</span>
      <span class="gap">PO Box 123456</span>
      <span>West 123456</span>
    </address>
  </article>

  <!-- Envelope, back -->
  <article class="envelope envelope--back" aria-label="Envelope back">
    <svg class="envelope__flap" viewBox="0 0 420 90" aria-hidden="true">
      <path d="M0,0 H420 V50 Q420,58 410,60 L10,60 Q0,58 0,50 Z" fill="var(--midnight)"/>
    </svg>
    <div class="envelope__back-logo">
      <span class="wordmark__name">Corvane Diamonds</span>
      <span class="tagline">FINE STONES TRADING HOUSE</span>
    </div>
  </article>

  <!-- Business card, front -->
  <article class="card card--front" aria-label="Business card front">
    <div class="wordmark"><span class="wordmark__mark"></span><span class="wordmark__name">Corvane Diamonds</span></div>
    <div class="tagline">FINE STONES TRADING HOUSE</div>
  </article>

  <!-- Business card, back -->
  <article class="card card--back" aria-label="Business card back">
    <svg class="card__pattern" viewBox="0 0 200 116" role="img" aria-label="Faceted geometric pattern in magenta, purple and pink tones">
      <defs>
        <linearGradient id="card-facets" x1="0" y1="0" x2="1" y2="1">
          <stop offset="0" stop-color="#3a1f63"/>
          <stop offset="0.4" stop-color="#c21b86"/>
          <stop offset="0.7" stop-color="#e35fa6"/>
          <stop offset="1" stop-color="#8d7fb0"/>
        </linearGradient>
      </defs>
      <polygon points="0,0 62,0 58,40 110,116 0,116" fill="url(#card-facets)"/>
    </svg>
    <div class="card__person">
      <p class="card__name">ALDEN VOSS</p>
      <p class="card__role">Managing Director</p>
    </div>
    <ul class="card__contacts">
      <li><svg viewBox="0 0 10 10" aria-hidden="true"><path d="M2 0.5 L4 2.5 L3 4 Q4.5 6 6 7 L7.5 6 L9.5 8 L8 9.5 Q3.5 9 0.5 2 Z"/></svg>+01 234 567 890</li>
      <li><svg viewBox="0 0 10 10" aria-hidden="true"><path d="M0.5 2 H9.5 V8 H0.5 Z M1 2.5 L5 5.5 L9 2.5" fill="none" stroke="#222" stroke-width="1"/></svg>hello@corvane.com</li>
      <li><svg viewBox="0 0 10 10" aria-hidden="true"><path d="M5 0.5 A3.3 3.3 0 0 1 8.3 3.8 C8.3 6 5 9.5 5 9.5 C5 9.5 1.7 6 1.7 3.8 A3.3 3.3 0 0 1 5 0.5 Z"/></svg>www.corvane.com</li>
    </ul>
  </article>

</main>
</body>
</html>
```